Birchline Septic Solutions

Would like to see some single sided ones but would also like to see some double sided with one sided only being the logo. Owners name is Tom Halvick. Phone number is 555-214-0387
Services are pumping, inspections, installs, and repairs

Contact Information for Business Card

555-241-0387 Tom Halvick Greenfield, OH

```html
<!DOCTYPE html>
<html lang="en">
<head>
<meta charset="utf-8">
<title>Birchline Septic Solutions – Business Card</title>
<link href="https://fonts.googleapis.com/css2?family=Lato:wght@400;700;900&family=Montserrat:wght@800&display=swap" rel="stylesheet">
<style>
  :root {
    --stage: #2b2c2f;
    --card-dark: #1b1c1d;
    --card-dark-soft: #242526;
    --card-light: #ffffff;
    --teal: #22bab5;
    --ink: #161616;
    --muted: #555a5e;
    --haze: #e9e9eb;
  }
  * { box-sizing: border-box; margin: 0; padding: 0; }
  html, body { width: 1200px; height: 952px; overflow: hidden; }
  body {
    background: var(--stage);
    display: flex;
    flex-direction: column;
    align-items: center;
    justify-content: center;
    gap: 44px;
    font-family: "Lato", sans-serif;
  }
  .card {
    position: relative;
    width: 700px;
    height: 400px;
    border-radius: 26px;
    overflow: hidden;
  }

  /* Front – logo side */
  .card--front { background: var(--card-dark); }
  .card--front .scenery {
    position: absolute;
    left: 0; right: 0; top: 70px; bottom: 92px;
    background: linear-gradient(180deg, var(--card-dark) 0%, var(--card-dark-soft) 55%, #2a2b2c 100%);
  }
  .card--front .wordmark {
    position: absolute;
    left: 0; right: 0; top: 112px;
    text-align: center;
    font-family: "Montserrat", sans-serif;
    font-weight: 800;
    font-size: 44px;
    line-height: 1.15;
    letter-spacing: 4px;
    color: #ffffff;
    text-transform: uppercase;
  }
  .card--front .rule {
    position: absolute;
    left: 0; right: 0; bottom: 92px;
    height: 3px;
    background: #d8d8d8;
  }
  .services {
    position: absolute;
    left: 0; right: 0; bottom: 0;
    height: 86px;
    background: var(--teal);
    display: flex;
    align-items: center;
    justify-content: center;
    gap: 22px;
    list-style: none;
    font-weight: 700;
    font-size: 22px;
    letter-spacing: 1.5px;
    color: var(--ink);
    text-transform: uppercase;
  }
  .services li::before { content: "• "; }

  /* Back – contact side */
  .card--back { background: var(--card-light); }
  .card--back .scenery {
    position: absolute;
    inset: 0;
    background: radial-gradient(ellipse 420px 230px at 34% 100%, var(--haze) 0%, rgba(233,233,235,0.6) 55%, rgba(255,255,255,0) 100%);
  }
  .contact {
    position: absolute;
    left: 54px; top: 44px;
  }
  .contact .name {
    font-weight: 900;
    font-size: 34px;
    letter-spacing: 1px;
    color: var(--teal);
    text-transform: uppercase;
  }
  .contact .role {
    font-size: 19px;
    color: var(--muted);
    margin-top: 2px;
  }
  .contact .divider {
    width: 60px; height: 2px;
    background: var(--ink);
    margin: 14px 0 18px;
  }
  .details { list-style: none; }
  .details li {
    display: flex;
    align-items: flex-start;
    gap: 12px;
    font-size: 17px;
    line-height: 1.3;
    color: #333;
    margin-bottom: 10px;
  }
  .icon {
    flex: none;
    width: 22px; height: 22px;
    border-radius: 4px;
    display: flex;
    align-items: center;
    justify-content: center;
  }
  .icon--dark { background: var(--ink); }
  .icon--teal { background: var(--teal); }
  .card--back .wordmark {
    position: absolute;
    right: 44px; top: 282px;
    text-align: right;
    font-family: "Montserrat", sans-serif;
    font-weight: 800;
    font-size: 28px;
    line-height: 1.2;
    letter-spacing: 3px;
    color: var(--ink);
    text-transform: uppercase;
  }
</style>
</head>
<body>

  <section class="card card--front" aria-label="Business card front">
    <div class="scenery" role="img" aria-label="Faint forest and mountain silhouette backdrop"></div>
    <div class="wordmark">Birchline<br>Septic Solutions</div>
    <div class="rule"></div>
    <ul class="services">
      <li>Pumping</li>
      <li>Inspections</li>
      <li>Installs</li>
      <li>Repairs</li>
    </ul>
  </section>

  <section class="card card--back" aria-label="Business card back">
    <div class="scenery" role="img" aria-label="Faint mountain peak and pine tree backdrop"></div>
    <div class="contact">
      <p class="name">Tom Halvick</p>
      <p class="role">Managing Director</p>
      <div class="divider"></div>
      <ul class="details">
        <li>
          <span class="icon icon--dark">
            <svg width="12" height="14" viewBox="0 0 12 14"><path d="M6 0a5 5 0 0 0-5 5c0 3.6 5 9 5 9s5-5.4 5-9a5 5 0 0 0-5-5zm0 7a2 2 0 1 1 0-4 2 2 0 0 1 0 4z" fill="#fff"/></svg>
          </span>
          <span>2718 Ridgeview Lane<br>Greenfield, OH</span>
        </li>
        <li>
          <span class="icon icon--teal">
            <svg width="13" height="13" viewBox="0 0 24 24"><path d="M6.6 10.8a15.1 15.1 0 0 0 6.6 6.6l2.2-2.2c.3-.3.7-.4 1-.2 1.1.4 2.3.6 3.6.6.6 0 1 .4 1 1V20c0 .6-.4 1-1 1A17 17 0 0 1 3 4c0-.6.4-1 1-1h3.5c.6 0 1 .4 1 1 0 1.3.2 2.5.6 3.6.1.3 0 .7-.2 1z" fill="#fff"/></svg>
          </span>
          <span>555-241-0387</span>
        </li>
        <li>
          <span class="icon icon--teal">
            <svg width="12" height="12" viewBox="0 0 12 12"><path d="M6 1 10 9H7.5L6 6 4.5 9H2z" fill="#fff"/></svg>
          </span>
          <span>www.birchlineseptic.example</span>
        </li>
      </ul>
    </div>
    <div class="wordmark">Birchline<br>Septic Solutions</div>
  </section>

</body>
</html>
```